Need Stunning Website for Talent Acquisition (Recruiting) Agency

Hello, I am seeking a very professional, high-quality website that reflects our Talent Acquisition agency, Cobalt Kin. Our agency slogan is "Talent Acquisition. Differently." We are in fact different - we are a full service agency that provides services most others do not, and our website needs to immediately reflect that something is different about us when they visit our site.

This contest is to do complete website design and coding, including all graphics, features, plugins, and design elements. The graphics are very important on the site and must be of the highest professional quality. One critical aspect is that the imagery must convey that we serve clients in a variety of industries, including business, healthcare, churches and religious organizations, non-profits, manufacturing, retail, and more. We recruit for both professional level positions (e.g. CEO, COO, Pastor), as well as entry level (e.g. secretary, caregiver, factory worker).
The following pages should be designed:
Home Page - a captivating home page that immediately tells our brand story, what makes us different, and the value that we bring to the table.
Client Services Page - a page that talks more about the services we provide and why we produce better results. This page will cover the 5 C's in greater detail as well as all the things that make us different.
Industries - The industries we serve
Request Services - a page where clients can submit details about a job they would like us to recruit for, including attaching a job description if they have one
Candidates Page - a simple page that encourages prospective candidates to submit their resume for review
About Us - Common about us page
Blog - Common blog page
Contact Us - a contact page for general inquiries
The website must be built in an ultra-SEO friendly manner and optimized for speed and performance. As mentioned above, you will be responsible for providing all graphics for the site (copyright compliant).
The website will need to be compatible with Elementor Pro (I have subscription) and Yoast SEO. It needs to be designed on a high-quality wordpress theme that receives regular updates. It also needs instant chat messaging feature. Would like a traditional menu bar at the top of the page (not a fan of menu's that are hidden or put on the side of the page).

Please, please, please - - do NOT waste my time with generic/stock templates, low-quality graphics, etc. We are a PREMIUM agency and our website needs to reflect that.

In the future we will add a job board - I do not want that initially - but will want the option to add it later.

Must also have the ability to upload documents /attachments on the contact page/form.

It probably goes without saying, but the page must be fully responsive - suitable to work on all device types.

Target Market(s)

Businesses

Industry/Entity Type

Talent Acquisition (Recruiting) Agency

Coding

Coded - Design and coding required

Number of Pages Required

5+ page

Requirements
Must have
• Please see brief
Should not have
• No generic template/stock website or graphics - must have PREMIUM feel.

```html
<!DOCTYPE html>
<html lang="en">
<head>
<meta charset="utf-8">
<title>Cobalt Kin — Talent Acquisition. Differently.</title>
<link href="https://fonts.googleapis.com/css2?family=Poppins:ital,wght@0,400;0,500;0,600;0,700;0,800;1,500;1,600;1,700;1,800&display=swap" rel="stylesheet">
<style>
:root{
  --navy:#141a4b;
  --navy-deep:#0f1440;
  --orange:#ffa400;
  --ink:#1c1f33;
  --muted:#8a8fa3;
  --line:#d9dbe3;
  --white:#ffffff;
}
*{box-sizing:border-box;margin:0;padding:0}
html,body{width:1200px;height:3333px;overflow:hidden;background:var(--white)}
body{font-family:"Poppins",sans-serif;color:var(--ink)}
.page{position:relative;width:1200px;height:3333px;overflow:hidden}
section,header,footer{position:relative;width:1200px}
.pill{display:inline-block;border-radius:30px;font-weight:600;font-size:14px;text-align:center}
.pill--orange{background:var(--orange);color:var(--navy)}
.pill--outline{border:2px solid var(--navy);color:var(--navy)}
.pill--outline-light{border:2px solid var(--white);color:var(--white)}
.heading{font-style:italic;font-weight:700;color:var(--orange)}

/* header */
.site-header{height:78px;display:flex;align-items:center;padding:0 70px;background:var(--white);z-index:2}
.brand{font-weight:700;font-size:40px;color:var(--navy);letter-spacing:-1px}
.nav{margin-left:auto;display:flex;gap:30px;align-items:center;font-size:14px;font-weight:600;color:var(--navy)}
.nav .active{color:var(--orange);position:relative}
.nav .active::after{content:"";position:absolute;left:-14px;right:-14px;top:-31px;height:3px;background:var(--orange)}
.lang{border:2px solid var(--orange);border-radius:20px;padding:2px 14px;font-size:11px}

/* hero */
.hero{height:520px;background:linear-gradient(90deg,#1d2566 0%,#222c6c 42%,#4c5680 70%,#7a8399 100%)}
.hero__photo{position:absolute;inset:0;background:linear-gradient(90deg,rgba(29,37,102,0) 40%,rgba(150,158,178,.35) 100%)}
.hero__copy{position:absolute;left:70px;top:130px;z-index:1}
.hero__title{font-style:italic;font-weight:800;font-size:48px;line-height:58px;color:var(--white)}
.hero__sub{margin-top:30px;font-style:italic;font-weight:700;font-size:17px;line-height:25px;color:var(--orange)}
.hero__copy .pill{margin-top:32px;padding:9px 32px}
.dots{position:absolute;left:562px;top:400px;display:flex;gap:14px;z-index:1}
.dots span{width:16px;height:16px;border:2px solid var(--white);border-radius:50%}
.dots .on{background:var(--orange);box-shadow:inset 0 0 0 3px var(--navy)}
.hero__curve{position:absolute;left:0;bottom:-120px;width:1200px;height:300px}

/* why */
.why{height:300px}
.why__brand{position:absolute;left:145px;top:110px;font-size:64px;font-weight:700;color:var(--navy);letter-spacing:-2px}
.why__body{position:absolute;left:618px;top:30px;width:460px}
.why__body h2{font-size:26px}
.why__body p{margin-top:14px;font-size:13px;line-height:21px;color:var(--muted)}
.why__body ul{margin-top:12px;list-style:none;font-size:12.5px;line-height:26px;color:var(--ink)}
.why__body li::before{content:"";display:inline-block;border-left:5px solid var(--orange);border-top:4px solid transparent;border-bottom:4px solid transparent;margin-right:10px}
.why__body .pill{margin-top:24px;padding:7px 32px}

/* services */
.services{height:700px}
.services__bg{position:absolute;inset:0;width:1200px;height:700px}
.services__title{position:absolute;top:110px;width:100%;text-align:center;font-size:44px}
.service{position:absolute;display:flex;gap:18px;width:340px}
.service__icon{flex:0 0 76px;height:76px;border-radius:50%;background:var(--orange);display:flex;align-items:center;justify-content:center}
.service h3{font-size:19px;font-weight:600;color:var(--white);line-height:24px;margin-top:4px}
.service p{font-size:11.5px;line-height:17px;color:#b8bcd6;margin-top:4px}
.services__photo{position:absolute;left:427px;top:198px;width:345px;height:345px;border-radius:50%;border:3px solid var(--orange);padding:6px}
.services__photo div{width:100%;height:100%;border-radius:50%;background:radial-gradient(circle,#f2f2f4 0%,#c9cbd3 60%,#8c90a3 100%)}
.services .pill{position:absolute;left:795px;top:462px;padding:7px 34px}

/* industries */
.industries{height:470px}
.industries__title{text-align:center;font-size:44px;padding-top:6px}
.grid{position:absolute;left:221px;top:95px;display:grid;grid-template-columns:repeat(3,242px);gap:16px 16px}
.tile{height:124px;border:1px solid var(--line);display:flex;flex-direction:column;align-items:center;justify-content:center;gap:14px;font-size:15px;font-weight:500;color:var(--ink)}
.industries .pill{position:absolute;left:528px;top:378px;padding:7px 34px}

/* audience */
.audience{height:340px}
.audience__bg{position:absolute;inset:0;width:1200px;height:340px}
.audience__col{position:absolute;top:105px;width:490px;text-align:center;color:var(--white)}
.audience__col h2{font-size:30px;font-weight:500}
.audience__col p{margin-top:10px;font-size:13px;line-height:21px}
.audience__col .pill{margin-top:22px;padding:6px 32px}
.audience__divider{position:absolute;left:600px;top:105px;width:1px;height:135px;background:rgba(255,255,255,.3)}

/* blogs */
.blogs{height:445px}
.blogs__title{text-align:center;font-size:44px;padding-top:2px}
.cards{position:absolute;left:95px;top:80px;display:flex;gap:25px}
.card{width:320px}
.card__img{height:190px}
.card p{margin-top:16px;font-size:13.5px;line-height:21px}
.card__meta{margin-top:12px;display:flex;align-items:center;gap:10px;font-size:11.5px;font-style:italic}
.card__meta .pill{font-size:11.5px;font-weight:500;font-style:italic;padding:3px 22px;border:1px solid var(--line);color:var(--ink);margin-left:12px}
.card__meta .pill--orange{border-color:var(--orange);color:var(--white)}
.blogs .view-all{position:absolute;left:535px;top:388px;padding:6px 34px}

/* footer */
.footer{height:480px;color:var(--white)}
.footer__bg{position:absolute;inset:0;width:1200px;height:480px}
.footer__brand{position:absolute;left:70px;top:125px;font-size:40px;font-weight:700;letter-spacing:-1px}
.footer h4{font-style:italic;font-weight:700;font-size:18px;color:var(--orange)}
.contact{position:absolute;left:70px;top:198px}
.contact li{list-style:none;display:flex;align-items:center;gap:24px;font-size:13.5px;margin-top:26px}
.links{position:absolute;left:345px;top:198px}
.links li{list-style:none;font-size:13.5px;margin-top:8px}
.links li:first-child{color:var(--orange);text-decoration:underline}
.footer__rule{position:absolute;left:500px;top:170px;width:1px;height:245px;background:rgba(255,255,255,.2)}
.inquire{position:absolute;left:542px;top:160px;width:590px}
.inquire h4{font-size:26px}
.inquire small{display:block;margin-top:4px;font-size:10.5px;color:#c8cbe0}
.form{margin-top:12px;display:grid;grid-template-columns:285px 285px;gap:0 16px}
.field{height:36px;background:rgba(255,255,255,.2);margin-bottom:10px;display:flex;align-items:center;gap:10px;padding:0 14px;font-size:11px}
.field--msg{grid-column:2;grid-row:1/4;height:128px;align-items:flex-start;padding-top:12px}
.inquire .pill{margin-top:2px;padding:6px 34px}
.to-top{position:absolute;right:10px;top:378px;width:48px;height:48px;border-radius:50%;background:var(--orange);display:flex;align-items:center;justify-content:center}
.copyright{position:absolute;left:0;bottom:0;width:1200px;height:40px;background:var(--orange);display:flex;align-items:center;padding:0 70px;font-size:11.5px;color:var(--navy)}
.social{margin-left:auto;display:flex;gap:10px}
.social span{width:20px;height:20px;border:1.5px solid var(--navy);border-radius:3px}
</style>
</head>
<body>
<div class="page">

<header class="site-header">
  <div class="brand">Cobalt Kin</div>
  <nav class="nav">
    <span class="active">Home</span><span>About Us</span><span>Our Services</span><span>Industries</span><span>Blogs</span><span>Contact Us</span>
    <span class="lang">EN ▾</span>
  </nav>
</header>

<section class="hero">
  <div class="hero__photo" role="img" aria-label="Photo of two professionals in a job interview at an office table"></div>
  <div class="hero__copy">
    <h1 class="hero__title">Talent Acquisition.<br>Differently.</h1>
    <p class="hero__sub">We recruit both Professional Level Positions,<br>as well as Entry Level</p>
    <a class="pill pill--orange">Schedule a Free Consultation</a>
  </div>
  <div class="dots"><span></span><span class="on"></span><span></span></div>
  <svg class="hero__curve" viewBox="0 0 1200 300" preserveAspectRatio="none">
    <path d="M0 120 C300 40 560 10 800 40 C980 62 1120 130 1200 200 L1200 300 L0 300 Z" fill="#ffa400"/>
    <path d="M0 130 C280 60 560 30 790 60 C960 82 1100 150 1200 240 L1200 300 L0 300 Z" fill="#fff"/>
    <path d="M220 70 C420 20 620 10 800 40 C980 62 1120 130 1200 200 L1200 160 C1120 90 980 30 800 14 C600 -4 420 20 220 70 Z" fill="#ffa400"/>
  </svg>
</section>

<section class="why">
  <div class="why__brand">Cobalt Kin</div>
  <div class="why__body">
    <h2 class="heading">Why Choose Us</h2>
    <p>Lorem Ipsum is simply dummy text of the printing and typesetting industry. Lorem Ipsum has been the industry's...</p>
    <ul>
      <li>Lorem ipsum dolor sit amet, consectetur adipiscing elit.</li>
      <li>Vivamus ac orci at magna aliquet sagittis id quis libero.</li>
      <li>Aenean eu est finibus, vehicula elit ut, tincidunt tortor.</li>
    </ul>
    <a class="pill pill--outline">About Us</a>
  </div>
</section>

<section class="services">
  <svg class="services__bg" viewBox="0 0 1200 700" preserveAspectRatio="none">
    <path d="M0 70 C200 -10 380 0 600 45 C820 90 1000 95 1200 40 L1200 700 L0 700 Z" fill="#141a4b"/>
    <path d="M0 700 L0 690 C200 610 450 570 700 572 C950 575 1100 610 1200 640 L1200 700 Z" fill="#fff"/>
  </svg>
  <h2 class="services__title heading">Our Services</h2>
  <div class="service" style="left:70px;top:205px">
    <div class="service__icon"><svg width="36" height="36" viewBox="0 0 36 36" fill="none" stroke="#141a4b" stroke-width="2"><circle cx="18" cy="18" r="14"/><circle cx="18" cy="15" r="5"/><path d="M9 28c3-6 15-6 18 0"/></svg></div>
    <div><h3>Correct hiring.</h3><p>Lorem Ipsum is simply dummy text of<br>the printing and typesetting...</p></div>
  </div>
  <div class="service" style="left:70px;top:325px">
    <div class="service__icon"><svg width="36" height="36" viewBox="0 0 36 36" fill="none" stroke="#141a4b" stroke-width="2"><rect x="7" y="8" width="22" height="20" rx="2"/><path d="M7 14h22M13 20h10M13 24h6"/></svg></div>
    <div><h3>Compensate fairly.</h3><p>Lorem Ipsum is simply dummy text of<br>the printing and typesetting...</p></div>
  </div>
  <div class="service" style="left:70px;top:445px">
    <div class="service__icon"><svg width="36" height="36" viewBox="0 0 36 36" fill="none" stroke="#141a4b" stroke-width="2"><circle cx="11" cy="11" r="5"/><circle cx="25" cy="11" r="5"/><circle cx="11" cy="25" r="5"/><circle cx="25" cy="25" r="5"/></svg></div>
    <div><h3>Currencies of choice.</h3><p>Lorem Ipsum is simply dummy text of<br>the printing and typesetting...</p></div>
  </div>
  <div class="services__photo"><div role="img" aria-label="Overhead photo of a team around a table with a network diagram"></div></div>
  <div class="service" style="left:795px;top:200px">
    <div class="service__icon"><svg width="36" height="36" viewBox="0 0 36 36" fill="none" stroke="#141a4b" stroke-width="2"><path d="M7 15h5l12-7v20l-12-7H7z"/><path d="M12 21l2 8"/></svg></div>
    <div><h3>Communicate with FOCUS.</h3><p>Lorem Ipsum is simply dummy text of<br>the printing and typesetting...</p></div>
  </div>
  <div class="service" style="left:795px;top:322px">
    <div class="service__icon"><svg width="36" height="36" viewBox="0 0 36 36" fill="none" stroke="#141a4b" stroke-width="2"><rect x="14" y="5" width="8" height="6"/><rect x="4" y="25" width="8" height="6"/><rect x="14" y="25" width="8" height="6"/><rect x="24" y="25" width="8" height="6"/><path d="M18 11v14M8 25v-6h20v6"/></svg></div>
    <div><h3>Classify and manage appropriately.</h3><p>Lorem Ipsum is simply dummy text of<br>the printing and typesetting...</p></div>
  </div>
  <a class="pill pill--orange">View All Services</a>
</section>

<section class="industries">
  <h2 class="industries__title heading">Industries</h2>
  <div class="grid">
    <div class="tile"><svg width="40" height="36" viewBox="0 0 40 36" fill="none" stroke="#ffa400" stroke-width="2"><path d="M4 34V16l10-6v6l10-6v6l10-6v24z"/><path d="M30 4v8"/></svg>Industries</div>
    <div class="tile"><svg width="40" height="36" viewBox="0 0 40 36" fill="none" stroke="#ffa400" stroke-width="2"><path d="M20 32 6 18a8 8 0 0 1 14-10 8 8 0 0 1 14 10z"/><path d="M8 18h8l3-5 4 9 3-4h6"/></svg>Healthcare</div>
    <div class="tile"><svg width="40" height="36" viewBox="0 0 40 36" fill="none" stroke="#ffa400" stroke-width="2"><path d="M20 2v8M16 6h8M10 34V18l10-8 10 8v16z"/><path d="M17 34v-8h6v8"/></svg>Churches</div>
    <div class="tile"><svg width="40" height="36" viewBox="0 0 40 36" fill="none" stroke="#ffa400" stroke-width="2"><path d="M20 2 34 10v16L20 34 6 26V10z"/><circle cx="20" cy="18" r="5"/></svg>Non-Profits</div>
    <div class="tile"><svg width="40" height="36" viewBox="0 0 40 36" fill="none" stroke="#ffa400" stroke-width="2"><path d="M4 34h32M8 34V20l8-5v5l8-5v5l8-5v19"/><path d="M12 26h4M20 26h4M28 26h2"/></svg>Manufacturing</div>
    <div class="tile"><svg width="40" height="36" viewBox="0 0 40 36" fill="none" stroke="#ffa400" stroke-width="2"><path d="M4 12 8 4h24l4 8z"/><path d="M6 12v22h28V12M15 34v-10h10v10"/></svg>Retail</div>
  </div>
  <a class="pill pill--orange">View More</a>
</section>

<section class="audience">
  <svg class="audience__bg" viewBox="0 0 1200 340" preserveAspectRatio="none">
    <defs><linearGradient id="aud" x1="0" x2="1"><stop offset="0" stop-color="#141a4b"/><stop offset=".45" stop-color="#1f2454"/><stop offset=".62" stop-color="#ffa400"/><stop offset="1" stop-color="#ffa400"/></linearGradient></defs>
    <path d="M0 45 C300 60 600 40 850 15 C1000 0 1120 -5 1200 10 L1200 300 C1050 270 850 255 600 270 C350 286 150 305 0 322 Z" fill="url(#aud)"/>
  </svg>
  <div class="audience__col" style="left:120px"><h2>Employers</h2><p>Lorem Ipsum is simply dummy text of the printing<br>and typesetting industry. Lorem Ipsum...</p><a class="pill pill--outline-light">Read More</a></div>
  <div class="audience__divider"></div>
  <div class="audience__col" style="left:610px"><h2>Candidates</h2><p>Lorem Ipsum is simply dummy text of the printing<br>and typesetting industry. Lorem Ipsum...</p><a class="pill pill--outline">Read More</a></div>
</section>

<section class="blogs">
  <h2 class="blogs__title heading">Blogs</h2>
  <div class="cards">
    <article class="card">
      <div class="card__img" role="img" aria-label="Photo of two colleagues shaking hands in an office" style="background:linear-gradient(135deg,#d8dce4,#6b7690)"></div>
      <p>Lorem Ipsum is simply dummy text of the printing and typesetting...</p>
      <div class="card__meta"><svg width="14" height="14" viewBox="0 0 14 14" fill="none" stroke="#ffa400" stroke-width="1.5"><rect x="1" y="2" width="12" height="11"/><path d="M1 5h12M4 0v3M10 0v3"/></svg>25 June, 2022<a class="pill">Read More</a></div>
    </article>
    <article class="card">
      <div class="card__img" role="img" aria-label="Photo of a smiling team gathered around a desk" style="background:linear-gradient(135deg,#e4e6ec,#5a6a88)"></div>
      <p>Lorem Ipsum is simply dummy text of the printing and typesetting...</p>
      <div class="card__meta"><svg width="14" height="14" viewBox="0 0 14 14" fill="none" stroke="#ffa400" stroke-width="1.5"><rect x="1" y="2" width="12" height="11"/><path d="M1 5h12M4 0v3M10 0v3"/></svg>25 June, 2022<a class="pill">Read More</a></div>
    </article>
    <article class="card">
      <div class="card__img" role="img" aria-label="Photo of a candidate in an interview at a bright office" style="background:linear-gradient(135deg,#eef0f3,#9aa3b4)"></div>
      <p>Lorem Ipsum is simply dummy text of the printing and typesetting...</p>
      <div class="card__meta"><svg width="14" height="14" viewBox="0 0 14 14" fill="none" stroke="#ffa400" stroke-width="1.5"><rect x="1" y="2" width="12" height="11"/><path d="M1 5h12M4 0v3M10 0v3"/></svg>25 June, 2022<a class="pill pill--orange">Read More</a></div>
    </article>
  </div>
  <a class="pill pill--outline view-all">View All</a>
</section>

<footer class="footer">
  <svg class="footer__bg" viewBox="0 0 1200 480" preserveAspectRatio="none">
    <path d="M0 0 C250 110 550 125 900 85 C1050 66 1140 40 1200 20 L1200 480 L0 480 Z" fill="#ffa400"/>
    <path d="M0 25 C250 130 550 145 900 105 C1050 86 1140 60 1200 50 L1200 480 L0 480 Z" fill="#141a4b"/>
  </svg>
  <div class="footer__brand">Cobalt Kin</div>
  <div class="contact">
    <h4>Conatct Info</h4>
    <ul>
      <li><svg width="16" height="18" viewBox="0 0 16 18" fill="#ffa400"><path d="M8 0a6 6 0 0 0-6 6c0 5 6 12 6 12s6-7 6-12a6 6 0 0 0-6-6zm0 8.5A2.5 2.5 0 1 1 8 3.5a2.5 2.5 0 0 1 0 5z"/></svg>Lindenweg, Canton Nord</li>
      <li><svg width="16" height="16" viewBox="0 0 16 16" fill="#ffa400"><path d="M3 1l3 3-2 2c1 2 3 4 5 5l2-2 3 3-2 3C7 15 1 9 1 3z"/></svg>+41 (0)79 555 0142</li>
      <li><svg width="16" height="14" viewBox="0 0 16 14" fill="none" stroke="#ffa400" stroke-width="1.6"><rect x="1" y="1" width="14" height="12"/><path d="M1 1l7 6 7-6"/></svg>hello@cobaltkin.com</li>
    </ul>
  </div>
  <div class="links">
    <h4>Quick Links</h4>
    <ul><li>Home</li><li>About Us</li><li>Our Services</li><li>Industries</li><li>Blogs</li><li>Contact Us</li></ul>
  </div>
  <div class="footer__rule"></div>
  <div class="inquire">
    <h4>Inquire Now!</h4>
    <small>We guarantee a returned phone call within 24 business hours.</small>
    <div class="form">
      <div class="field">◯&nbsp; Name</div>
      <div class="field field--msg">▭&nbsp; Message</div>
      <div class="field">✉&nbsp; Email</div>
      <div class="field">▯&nbsp; Phone</div>
    </div>
    <a class="pill pill--outline-light">Submit</a>
  </div>
  <div class="to-top"><svg width="18" height="18" viewBox="0 0 18 18" fill="none" stroke="#fff" stroke-width="2"><path d="M3 2h12M9 16V6M5 10l4-4 4 4"/></svg></div>
  <div class="copyright">© Copyright 2022 Cobalt Kin. All Rights Reserved.
    <div class="social"><span></span><span></span><span></span><span></span></div>
  </div>
</footer>

</div>
</body>
</html>
```